Bright Harbor Galas one stop event solution

A new event company base in Singapore.
Specialist in PARTIES & SPECIAL EVENTS
FULL EVENT ORGANIZERS

Bright Harbor Galas provide all events need ranging from small to large number of people who are looking for a different way of organizing their event. We have a team of talented experience people working in a team to make your event more memorable moments...
Updates

Project Deadline Extended Reason: Date line is to rush would like to give them more time and more time for me to think Added Sunday, August 2, 2015

Target Market(s)

Club
Embassy
Pubs
Organisation
Community Events
ETC

Industry/Entity Type

Entertainment Industry

Font styles to use
Script

Colors
000000
fec214

Requirements
Must have
• anything that related to entertainment and event...
Nice to have
• Must be in gold and black color for the theme... wording and graphic in gold while the base background will be black...
Should not have
• Non

```html
<!DOCTYPE html>
<html lang="en">
<head>
<meta charset="UTF-8">
<title>Bright Harbor Galas – Flyer</title>
<link href="https://fonts.googleapis.com/css2?family=Great+Vibes&family=Poppins:wght@600&family=Varela+Round&display=swap" rel="stylesheet">
<style>
  :root {
    --black: #000000;
    --ink: #0b0b0b;
    --gold: #fec214;
    --gold-deep: #b8860b;
    --gold-light: #ffe37a;
    --white: #ffffff;
  }
  * { margin: 0; padding: 0; box-sizing: border-box; }
  html, body { width: 849px; height: 1200px; overflow: hidden; background: var(--black); }
  .flyer {
    position: relative;
    width: 849px;
    height: 1200px;
    background: radial-gradient(ellipse at 50% 28%, #171717 0%, var(--black) 60%);
    font-family: "Varela Round", sans-serif;
    color: var(--white);
    overflow: hidden;
  }
  .event-glow {
    position: absolute;
    top: 170px;
    left: 50%;
    width: 300px;
    height: 300px;
    margin-left: -150px;
    border-radius: 50%;
    background: radial-gradient(circle, rgba(255,227,122,0.9) 0%, rgba(254,194,20,0.55) 22%, rgba(184,134,11,0.18) 50%, rgba(0,0,0,0) 70%);
  }
  .brand {
    position: absolute;
    top: 500px;
    left: 0;
    width: 100%;
    text-align: center;
  }
  .brand-name {
    font-family: "Poppins", sans-serif;
    font-weight: 600;
    font-size: 46px;
    line-height: 56px;
    color: var(--gold);
    letter-spacing: 1px;
    text-transform: uppercase;
  }
  .brand-tagline {
    margin-top: 4px;
    font-family: "Poppins", sans-serif;
    font-weight: 600;
    font-size: 17px;
    color: var(--gold);
    letter-spacing: 1px;
    text-transform: uppercase;
  }
  .message {
    position: absolute;
    top: 628px;
    left: 0;
    width: 100%;
    text-align: center;
    font-family: "Great Vibes", cursive;
    font-size: 46px;
    line-height: 57px;
    color: var(--white);
  }
  .contacts {
    position: absolute;
    left: 52px;
    top: 968px;
    list-style: none;
    font-size: 22px;
    color: var(--white);
  }
  .contacts li {
    display: flex;
    align-items: center;
    height: 41px;
  }
  .contacts svg { width: 20px; height: 20px; margin-right: 32px; fill: var(--white); }
  .footer-wave {
    position: absolute;
    left: 0;
    bottom: 0;
    width: 849px;
    height: 130px;
  }
  .website {
    position: absolute;
    right: 48px;
    bottom: 70px;
    font-size: 22px;
    color: var(--ink);
  }
</style>
</head>
<body>
  <main class="flyer">
    <div class="event-glow" role="img" aria-label="Golden spotlight glow for the celebration"></div>

    <header class="brand">
      <div class="brand-name">Bright Harbor Galas</div>
      <div class="brand-tagline">One stop all your event need</div>
    </header>

    <p class="message">
      Kindly mention the details<br>
      which you want<br>
      on this design<br>
      and contact details
    </p>

    <ul class="contacts">
      <li>
        <svg viewBox="0 0 24 24"><path d="M6.6 10.8a15 15 0 0 0 6.6 6.6l2.2-2.2a1 1 0 0 1 1-.25 11.4 11.4 0 0 0 3.6.57 1 1 0 0 1 1 1V20a1 1 0 0 1-1 1A17 17 0 0 1 3 4a1 1 0 0 1 1-1h3.5a1 1 0 0 1 1 1c0 1.25.2 2.45.57 3.57a1 1 0 0 1-.25 1z"/></svg>
        00.00.00.0000
      </li>
      <li>
        <svg viewBox="0 0 24 24"><path d="M6 2h10v5H6zM4 8h16a2 2 0 0 1 2 2v6h-4v6H6v-6H2v-6a2 2 0 0 1 2-2zm4 9v3h8v-3z"/></svg>
        00.00.00.0000
      </li>
      <li>
        <svg viewBox="0 0 24 24"><path d="M2 5h20v14H2zm2 2v.5l8 5 8-5V7z"/></svg>
        yourname@yourwebsite.com
      </li>
    </ul>

    <svg class="footer-wave" viewBox="0 0 849 130" preserveAspectRatio="none">
      <defs>
        <linearGradient id="goldBand" x1="0" y1="0" x2="1" y2="0">
          <stop offset="0" stop-color="#b8860b"/>
          <stop offset="0.5" stop-color="#ffe37a"/>
          <stop offset="1" stop-color="#fec214"/>
        </linearGradient>
      </defs>
      <path d="M0 60 C 250 150, 520 -10, 849 20 L 849 130 L 0 130 Z" fill="url(#goldBand)"/>
      <path d="M0 72 C 230 160, 480 40, 849 92 L 849 130 L 0 130 Z" fill="#000000"/>
      <path d="M0 96 C 240 170, 500 70, 849 112" fill="none" stroke="#fec214" stroke-width="3"/>
      <path d="M0 118 C 260 170, 540 100, 849 128 L 849 130 L 0 130 Z" fill="url(#goldBand)"/>
    </svg>
    <div class="website">www.yourwebsite.com</div>
  </main>
</body>
</html>
```